Alcohol brand needs design for gift tin packaging

We need a new design for the gift tins for our vodka brand. The bottles are in the shape of an oil barrel and the tins are also in the same shape. We would like to see the use of our logo. The gift tin needs to have a premium look.
Images of our bottles, logo and the gift tin are attached.

```html
<!DOCTYPE html>
<html lang="en">
<head>
<meta charset="utf-8">
<title>Iron Drum Vodka – Gift Tin Wrap</title>
<link rel="stylesheet" href="https://fonts.googleapis.com/css2?family=Special+Elite&family=IM+Fell+English+SC&display=swap">
<style>
  :root {
    --page: #ffffff;
    --tin-light: #e4e4e4;
    --tin-mid: #cfcfcf;
    --tin-dark: #a9a9a9;
    --ridge-hi: #f4f4f4;
    --ridge-lo: #8e8e8e;
    --ink: #151515;
  }
  * { margin: 0; padding: 0; box-sizing: border-box; }
  html, body {
    width: 1200px; height: 934px; overflow: hidden;
    background: var(--page);
  }
  .canvas {
    position: relative; width: 1200px; height: 934px;
    display: flex; align-items: center; justify-content: center;
  }
  .tin-wrap {
    position: relative; width: 560px; height: 780px;
    border-radius: 10px;
    background: linear-gradient(90deg, var(--tin-dark) 0%, var(--tin-mid) 14%, var(--tin-light) 45%, var(--tin-mid) 80%, var(--tin-dark) 100%);
    border: 2px solid var(--ridge-lo);
    color: var(--ink);
    font-family: "Special Elite", "Courier New", monospace;
    text-align: center;
  }
  .rim {
    position: absolute; left: 0; right: 0; height: 14px;
    background: linear-gradient(180deg, var(--ridge-hi), var(--tin-dark));
  }
  .rim--top { top: 0; border-radius: 8px 8px 0 0; }
  .rim--bottom { bottom: 0; border-radius: 0 0 8px 8px; }
  .ridge {
    position: absolute; left: 0; right: 0; height: 12px;
    background: linear-gradient(180deg, var(--ridge-hi) 0%, var(--tin-mid) 45%, var(--ridge-lo) 100%);
  }
  .ridge--upper { top: 258px; }
  .ridge--lower { top: 520px; }
  .band { position: absolute; left: 0; right: 0; }
  .band--title { top: 90px; }
  .brand-name { font-size: 62px; letter-spacing: 1px; line-height: 1; }
  .brand-type { font-size: 44px; margin-top: 14px; letter-spacing: 2px; }
  .band--emblem {
    top: 290px; height: 210px;
    display: flex; align-items: center; justify-content: space-between;
    padding: 0 70px;
  }
  .since, .strength { font-size: 30px; line-height: 1.05; }
  .strength .pct { font-size: 40px; display: block; }
  .strength .label { font-size: 26px; }
  .emblem {
    display: flex; flex-direction: column; align-items: center; gap: 12px;
    font-size: 26px; letter-spacing: 1px;
  }
  .emblem-dot { width: 110px; height: 110px; border-radius: 50%; background: var(--ink); }
  .band--footer { top: 580px; }
  .caution { font-size: 40px; letter-spacing: 1px; }
  .origin {
    font-family: "IM Fell English SC", Georgia, serif;
    font-size: 22px; margin-top: 20px; letter-spacing: 1px;
  }
  .volume {
    font-family: "IM Fell English SC", Georgia, serif;
    font-size: 22px; margin-top: 8px;
  }
</style>
</head>
<body>
<main class="canvas">
  <section class="tin-wrap">
    <div class="rim rim--top"></div>

    <header class="band band--title">
      <h1 class="brand-name">IRON DRUM</h1>
      <p class="brand-type">VODKA</p>
    </header>

    <div class="ridge ridge--upper"></div>

    <div class="band band--emblem">
      <p class="since">SINCE<br>2017</p>
      <div class="emblem">
        <span class="emblem-dot"></span>
        <span class="emblem-name">IRON DRUM</span>
      </div>
      <p class="strength"><span class="pct">40%</span><span class="label">ALCOHOL</span></p>
    </div>

    <div class="ridge ridge--lower"></div>

    <footer class="band band--footer">
      <p class="caution">DRINK CAUTIOUSLY</p>
      <p class="origin">Premium Australian Vodka</p>
      <p class="volume">700ML</p>
    </footer>

    <div class="rim rim--bottom"></div>
  </section>
</main>
</body>
</html>
```